Red Sea Boat trips in need of Business Card for Private Boat Tours

We need a Business card for a new business set-up in Egypt on the Red Sea for private snorkelling and boat excursions to one of the world's most beautiful reefs. We have wording logo already set-up which matches the boat but we need business cards to be bright and colourful with pictures of boat

Industry/Entity Type

Tourism

Contact Information for Business Card

Two Silver Herons (font provided) Boat Trips

```html
<!DOCTYPE html>
<html lang="en">
<head>
<meta charset="utf-8">
<title>Two Silver Herons – Business Card</title>
<link rel="stylesheet" href="https://fonts.googleapis.com/css2?family=Open+Sans:wght@400;600&family=Yellowtail&display=swap">
<style>
  :root {
    --backdrop: #e6e6e4;
    --card: #2f3032;
    --card-edge: #1f2021;
    --logo-grey: #9a9b9d;
    --teal: #1f8fa6;
    --text-light: #f1f2f3;
    --text-muted: #8c8e90;
    --reef-deep: #12303a;
    --reef-mid: #2b6d78;
    --reef-coral: #7a6a3a;
    --lagoon-light: #8fd3d6;
    --lagoon-mid: #4fb3bb;
    --sand: #bfe6e4;
  }
  * { box-sizing: border-box; margin: 0; padding: 0; }
  html, body { width: 1200px; height: 804px; overflow: hidden; }
  body {
    background: var(--backdrop);
    font-family: "Open Sans", Arial, sans-serif;
    position: relative;
  }
  .card {
    position: absolute;
    width: 640px;
    height: 360px;
    background: var(--card);
    border-radius: 4px;
    overflow: hidden;
    box-shadow: 0 10px 24px rgba(0,0,0,.22);
  }
  .card--front { left: 40px; top: 28px; }
  .card--back { left: 520px; top: 414px; }

  /* front */
  .reef-photo {
    position: absolute;
    inset: 0 0 0 120px;
    background:
      radial-gradient(ellipse at 78% 30%, var(--reef-coral) 0%, transparent 40%),
      radial-gradient(ellipse at 40% 85%, #3c4a46 0%, transparent 45%),
      linear-gradient(160deg, var(--reef-mid) 0%, var(--reef-deep) 55%, #1a2b2c 100%);
    -webkit-mask-image: linear-gradient(100deg, transparent 0%, #000 40%);
            mask-image: linear-gradient(100deg, transparent 0%, #000 40%);
  }
  .front-logo {
    position: absolute;
    left: 40px;
    top: 70px;
    font-size: 40px;
    font-weight: 600;
    color: var(--logo-grey);
    letter-spacing: .5px;
  }

  /* back */
  .lagoon-photo {
    position: absolute;
    top: 0; right: 0; bottom: 0;
    width: 330px;
    background:
      radial-gradient(ellipse at 70% 90%, #8b7a52 0%, transparent 35%),
      radial-gradient(ellipse at 55% 55%, var(--sand) 0%, transparent 55%),
      linear-gradient(170deg, var(--reef-mid) 0%, var(--lagoon-mid) 35%, var(--lagoon-light) 100%);
    -webkit-mask-image: linear-gradient(90deg, transparent 0%, #000 22%);
            mask-image: linear-gradient(90deg, transparent 0%, #000 22%);
  }
  .back-logo {
    position: absolute;
    left: 40px;
    top: 34px;
    font-size: 26px;
    font-weight: 600;
    color: var(--logo-grey);
  }
  .contact {
    position: absolute;
    left: 40px;
    top: 104px;
  }
  .contact__name {
    font-family: "Yellowtail", cursive;
    font-size: 38px;
    color: var(--teal);
    line-height: 1;
  }
  .contact__role {
    font-size: 18px;
    color: var(--text-muted);
    margin-top: 2px;
  }
  .contact__address {
    font-size: 19px;
    color: var(--text-light);
    line-height: 1.3;
    margin-top: 22px;
  }
  .contact__list {
    list-style: none;
    margin-top: 20px;
    font-size: 19px;
    color: var(--text-light);
    line-height: 1.35;
  }
  .contact__list li { display: flex; align-items: center; gap: 8px; }
  .contact__list svg { width: 16px; height: 16px; fill: var(--teal); flex: none; }
</style>
</head>
<body>
  <section class="card card--front">
    <div class="reef-photo" role="img" aria-label="Underwater photo of a coral reef with shoals of dark and orange fish"></div>
    <div class="front-logo">Two Silver Herons</div>
  </section>

  <section class="card card--back">
    <div class="lagoon-photo" role="img" aria-label="Underwater photo of a snorkeller with fins diving over a sandy lagoon and coral"></div>
    <div class="back-logo">Two Silver Herons</div>
    <div class="contact">
      <div class="contact__name">Daniel Hartley</div>
      <div class="contact__role">Managing Director</div>
      <div class="contact__address">Your Address, City<br>State, Zip 0000</div>
      <ul class="contact__list">
        <li>
          <svg viewBox="0 0 16 16" aria-hidden="true"><path d="M3 10c0-3 2-5 5-5s5 2 5 5v2H3z M1 5c2-3 12-3 14 0l-1 2h-3V5H5v2H2z"/></svg>
          044-123 456 789
        </li>
        <li>
          <svg viewBox="0 0 16 16" aria-hidden="true"><path d="M1 3h14v10H1z" fill="none" stroke="#1f8fa6" stroke-width="1.6"/><path d="M1 3l7 6 7-6" fill="none" stroke="#1f8fa6" stroke-width="1.6"/></svg>
          info@webname.com
        </li>
        <li>
          <svg viewBox="0 0 16 16" aria-hidden="true"><circle cx="8" cy="8" r="7"/><path d="M5 4c2 1 1 3 3 3s1 3 0 5M10 3c0 2 2 2 3 3" fill="none" stroke="#2f3032" stroke-width="1.2"/></svg>
          www.websitename.com
        </li>
      </ul>
    </div>
  </section>
</body>
</html>
```